Business card (AI file uploaded)

We need a business card design that is minimalist using existing logo (attached). Source files must be editable so we can make the same design with other names.

Screenshots included of a design I was working on to give you an idea of the style I would like. Looking for similar modern styles

Thanks

```html
<!DOCTYPE html>
<html lang="en">
<head>
<meta charset="utf-8">
<title>Quillmere Law Group — Business Card</title>
<link href="https://fonts.googleapis.com/css2?family=Exo+2:wght@500;600&family=Open+Sans:wght@400&display=swap" rel="stylesheet">
<style>
  :root {
    --backdrop: #3b3c3f;
    --card: #f7f7f7;
    --card-edge: #e6e6e6;
    --ink: #2f2f31;
    --band: #333335;
    --band-text: #ffffff;
    --rule: #5c5c5e;
  }
  html, body {
    margin: 0;
    padding: 0;
    width: 1200px;
    height: 816px;
    overflow: hidden;
    background: var(--backdrop);
  }
  .card {
    position: absolute;
    left: 100px;
    top: 123px;
    width: 1000px;
    height: 570px;
    border-radius: 40px;
    background: linear-gradient(160deg, #ffffff 0%, var(--card) 55%, var(--card-edge) 100%);
    overflow: hidden;
    font-family: "Open Sans", sans-serif;
    color: var(--ink);
  }
  .brand-mark {
    position: absolute;
    left: 500px;
    top: 212px;
    width: 76px;
    height: 76px;
    border-radius: 50%;
    background: var(--ink);
  }
  .brand-name {
    margin: 0;
    font-weight: 400;
  }
  .brand-primary {
    position: absolute;
    left: 592px;
    top: 186px;
    font-size: 58px;
    line-height: 60px;
    letter-spacing: 1px;
    white-space: nowrap;
  }
  .brand-secondary {
    position: absolute;
    left: 596px;
    top: 272px;
    font-size: 24px;
    line-height: 28px;
    letter-spacing: 6px;
    white-space: nowrap;
  }
  .rule-left {
    position: absolute;
    left: 370px;
    width: 130px;
    top: 298px;
    height: 4px;
    background: var(--rule);
  }
  .rule-right {
    position: absolute;
    left: 820px;
    right: 0;
    top: 298px;
    height: 4px;
    background: var(--rule);
  }
  .name-band {
    position: absolute;
    left: 0;
    top: 285px;
    width: 372px;
    height: 96px;
    background: var(--band);
    border-top-right-radius: 48px;
    color: var(--band-text);
    text-align: center;
    box-sizing: border-box;
    padding: 14px 30px 0 40px;
  }
  .person-name {
    font-family: "Exo 2", sans-serif;
    font-weight: 600;
    font-size: 30px;
    line-height: 38px;
    margin: 0;
  }
  .person-title {
    font-family: "Exo 2", sans-serif;
    font-weight: 500;
    font-size: 19px;
    letter-spacing: 2px;
    line-height: 28px;
    margin: 0;
  }
  .contacts {
    position: absolute;
    left: 40px;
    top: 408px;
    list-style: none;
    margin: 0;
    padding: 0;
    font-size: 19px;
  }
  .contacts li {
    display: flex;
    align-items: center;
    height: 42px;
  }
  .contacts svg, .address svg {
    width: 20px;
    height: 20px;
    margin-right: 18px;
    fill: var(--ink);
    flex: none;
  }
  .address {
    position: absolute;
    left: 640px;
    top: 352px;
    display: flex;
    align-items: flex-start;
    font-size: 19px;
    line-height: 28px;
    font-style: normal;
  }
  .address svg { margin-top: 18px; }
</style>
</head>
<body>
  <div class="card">
    <div class="brand-mark"></div>
    <h1 class="brand-name">
      <span class="brand-primary">QUILLMERE</span>
      <span class="brand-secondary">LAW GROUP</span>
    </h1>
    <div class="rule-left"></div>
    <div class="rule-right"></div>

    <div class="name-band">
      <p class="person-name">Daniel Harker</p>
      <p class="person-title">GENERAL MANAGER</p>
    </div>

    <ul class="contacts">
      <li>
        <svg viewBox="0 0 24 24" aria-hidden="true"><path d="M6.6 10.8a15.1 15.1 0 0 0 6.6 6.6l2.2-2.2a1 1 0 0 1 1-.25 11.4 11.4 0 0 0 3.6.57 1 1 0 0 1 1 1V20a1 1 0 0 1-1 1A17 17 0 0 1 3 4a1 1 0 0 1 1-1h3.5a1 1 0 0 1 1 1c0 1.25.2 2.45.57 3.57a1 1 0 0 1-.25 1z"/></svg>
        +1 (0222) 45-678-90
      </li>
      <li>
        <svg viewBox="0 0 24 24" aria-hidden="true"><path d="M2 5h20v14H2z M3.5 6.5 12 13l8.5-6.5" fill="none" stroke="#2f2f31" stroke-width="2"/><path d="M2 5h20l-10 8z"/></svg>
        info@quillmerelaw.com
      </li>
      <li>
        <svg viewBox="0 0 24 24" aria-hidden="true"><g fill="none" stroke="#2f2f31" stroke-width="1.8"><circle cx="12" cy="12" r="9.5"/><ellipse cx="12" cy="12" rx="4" ry="9.5"/><path d="M2.5 12h19M4 7h16M4 17h16"/></g></svg>
        www.quillmerelaw.com
      </li>
    </ul>

    <address class="address">
      <svg viewBox="0 0 24 24" aria-hidden="true"><path d="M12 3 2 12h3v8h5v-5h4v5h5v-8h3z"/></svg>
      <span>1450 Linden Street,<br>NW Arlington, USA</span>
    </address>
  </div>
</body>
</html>
```